Home Equity Lines of Credit
are BACK!!!

* Up to 97.5% on Owner Occupied Properties
* 700 Minimum Scores
* Fund in only 2-3 weeks

Can be used for...
* Education Expense
* Bill Consolidation
* Home Improvement
* Investments

Call today for more information!
(800) 647-2915

Bluecrest Lending Partners, Inc.
NMLS #318660
www.bluecrestlendhub.com

```html
<!DOCTYPE html>
<html lang="en">
<head>
<meta charset="utf-8">
<title>Home Equity Lines of Credit – Bluecrest Lending Partners</title>
<link rel="stylesheet" href="https://fonts.googleapis.com/css2?family=Montserrat:wght@400;500;700;800&family=Oswald:wght@500&display=swap">
<style>
  :root{
    --blue:#0b4f8c;
    --blue-deep:#093f70;
    --gold:#ad9b36;
    --gold-light:#d4c990;
    --white:#ffffff;
    --ink:#0d3f73;
    --rule:#6b6b6b;
  }
  *{margin:0;padding:0;box-sizing:border-box}
  html,body{width:1200px;height:1200px;overflow:hidden;background:var(--white)}
  .flyer{position:relative;width:1200px;height:1200px;font-family:"Montserrat",sans-serif;color:var(--ink)}
  .backdrop{position:absolute;inset:0}
  .brand{position:absolute;display:flex;align-items:center;gap:10px;font-weight:700;color:var(--blue)}
  .brand-dot{width:20px;height:20px;border-radius:50%;background:var(--gold);flex:none}
  .brand--top{left:52px;top:90px;width:250px;font-size:19px;line-height:1.25}
  .brand--bottom{left:440px;top:1030px;width:290px;font-size:20px;line-height:1.25}
  .headline{position:absolute;left:270px;top:395px;width:600px;text-align:center;color:var(--white);font-weight:500;font-size:64px;line-height:66px;letter-spacing:1px}
  .headline strong{font-weight:800}
  .uses{position:absolute;left:445px;top:670px;width:300px;text-align:center;color:var(--white);font-family:"Oswald",sans-serif;font-weight:500;text-transform:uppercase}
  .uses-lead{font-size:27px;margin-bottom:4px}
  .uses-list{list-style:none;width:244px;margin:0 auto}
  .uses-list li{font-size:29px;line-height:44px;border-top:1.5px solid rgba(255,255,255,.85)}
  .uses-list li:first-child{border-top:none}
  .uses-stars{font-size:18px;letter-spacing:12px;margin-top:2px}
  .perks{position:absolute;left:49px;top:948px;width:360px;list-style:none}
  .perks li{display:flex;align-items:center;gap:18px;font-weight:800;font-size:21.5px;line-height:1.2;color:var(--ink);padding:8px 0;border-top:1px solid var(--rule)}
  .perks li:first-child{border-top:none;padding-top:0}
  .perks em{font-style:normal;color:var(--gold)}
  .perks svg{flex:none;width:38px;height:38px}
  .contact{position:absolute;left:776px;top:1015px;width:380px}
  .contact-pill{background:var(--blue-deep);color:var(--white);border-radius:14px;font-size:15.5px;font-weight:500;text-align:center;height:27px;line-height:27px;letter-spacing:.3px;white-space:nowrap}
  .contact-phone{display:flex;align-items:center;gap:10px;margin-top:10px;white-space:nowrap}
  .contact-phone svg{flex:none}
  .contact-phone span{font-size:38px;font-weight:500;color:var(--ink);letter-spacing:.5px;line-height:1}
  .contact-web{text-align:center;color:var(--gold);font-weight:700;font-size:18px;margin-top:4px;padding-left:40px;white-space:nowrap}
  .footer{position:absolute;left:0;top:1155px;width:1200px;height:33px;display:flex;font-size:15px;color:var(--white)}
  .footer-name{width:406px;background:var(--gold);font-weight:800;font-size:17px;display:flex;align-items:center;justify-content:center;padding-left:20px}
  .footer-info{flex:1;background:var(--blue);display:flex;align-items:center;padding-left:36px;gap:12px;white-space:nowrap}
  .footer-sep{width:1.5px;height:24px;background:var(--white);margin:0 8px}
</style>
</head>
<body>
<div class="flyer">
  <svg class="backdrop" viewBox="0 0 1200 1200" width="1200" height="1200">
    <path d="M0 196 C110 200 200 222 240 240 C150 258 60 300 0 340 Z" fill="var(--gold)"/>
    <g role="img" aria-label="Photo of a smiling couple on a sofa looking at a tablet">
      <path d="M290 232 C430 110 620 38 820 28 C980 22 1110 60 1200 104 L1200 431 C1080 420 960 370 830 305 C660 228 480 206 290 232 Z" fill="#d9cfc5"/>
    </g>
    <g role="img" aria-label="Blue-tinted photo of a parent and child">
      <defs>
        <linearGradient id="blueTint" x1="0" y1="0" x2="1" y2="1">
          <stop offset="0" stop-color="#1a6aa8"/>
          <stop offset="1" stop-color="#074377"/>
        </linearGradient>
      </defs>
      <path d="M0 356 C110 290 220 255 330 252 C560 248 760 330 920 395 C1030 440 1120 458 1200 454 L1200 470 C1100 560 900 700 600 720 C400 735 150 700 0 660 Z" fill="url(#blueTint)"/>
    </g>
    <path d="M0 660 C150 700 400 735 600 720 C900 700 1100 560 1200 470 L1200 490 C1120 600 950 760 650 795 C400 815 150 770 0 730 Z" fill="var(--gold)"/>
    <path d="M0 730 C150 770 400 815 650 795 C950 760 1080 650 1140 590 C1090 700 960 800 700 830 C420 860 150 810 0 780 Z" fill="var(--gold-light)"/>
    <circle cx="181" cy="727" r="189" fill="var(--white)"/>
    <g role="img" aria-label="Photo of a smiling graduate in cap and gown holding a diploma">
      <circle cx="181" cy="727" r="181" fill="#3f4a5c"/>
    </g>
    <circle cx="1015" cy="716" r="189" fill="var(--white)"/>
    <g role="img" aria-label="Photo of a couple holding painting tools during home renovation">
      <circle cx="1015" cy="716" r="181" fill="#cdc6c0"/>
    </g>
    <circle cx="595" cy="783" r="162" fill="var(--white)"/>
    <circle cx="595" cy="783" r="151" fill="var(--gold)"/>
  </svg>

  <div class="brand brand--top"><span class="brand-dot"></span>Bluecrest Lending Partners, Inc.</div>

  <h1 class="headline">HOME EQUITY LINES OF CREDIT ARE <strong>BACK!!!</strong></h1>

  <div class="uses">
    <p class="uses-lead">Can be used for...</p>
    <ul class="uses-list">
      <li>Education Expense</li>
      <li>Bill Consolidation</li>
      <li>Home Improvement</li>
      <li>Investments</li>
    </ul>
    <p class="uses-stars">★★★</p>
  </div>

  <ul class="perks">
    <li>
      <svg viewBox="0 0 40 40" fill="none" stroke="var(--gold)" stroke-width="2.4" stroke-linejoin="round"><path d="M10 20 L20 11 L30 20 M13 18 V27 H27 V18"/><path d="M3 30 C10 28 14 30 20 32 C26 34 32 30 37 27"/></svg>
      <span>Up to <em>97.5%</em> on Owner Occupied Properties</span>
    </li>
    <li>
      <svg viewBox="0 0 40 40" fill="none" stroke="var(--gold)" stroke-width="2.4"><rect x="9" y="7" width="22" height="29" rx="2"/><rect x="15" y="4" width="10" height="6" rx="1"/><path d="M13 17h4M20 17h7M13 24h4M20 24h7M13 31h4"/></svg>
      <span><em>700</em> Minimum Scores</span>
    </li>
    <li>
      <svg viewBox="0 0 40 40" fill="none" stroke="var(--gold)" stroke-width="2.4"><rect x="5" y="8" width="30" height="27" rx="3"/><path d="M5 16h30M12 4v8M28 4v8M13 22v10M20 22v10M27 22v10M5 27h30"/></svg>
      <span>Fund in only <em>2-3</em> weeks</span>
    </li>
  </ul>

  <div class="brand brand--bottom"><span class="brand-dot"></span>Bluecrest Lending Partners, Inc.</div>

  <div class="contact">
    <p class="contact-pill">CALL TODAY FOR MORE INFORMATION!</p>
    <div class="contact-phone">
      <svg width="46" height="50" viewBox="0 0 56 60" fill="var(--ink)"><rect x="14" y="2" width="32" height="54" rx="5"/><rect x="18" y="9" width="24" height="38" fill="var(--white)"/><circle cx="30" cy="52" r="2" fill="var(--white)"/><path d="M2 24 C2 18 8 16 14 18 V44 C8 46 2 42 2 36 Z"/><rect x="42" y="20" width="10" height="5" rx="2.5"/><rect x="42" y="28" width="10" height="5" rx="2.5"/><rect x="42" y="36" width="10" height="5" rx="2.5"/></svg>
      <span>(800) 647-2915</span>
    </div>
    <p class="contact-web">www.bluecrestlendhub.com</p>
  </div>

  <div class="footer">
    <div class="footer-name">Bluecrest Lending Partners, Inc.</div>
    <div class="footer-info">
      <svg width="12" height="16" viewBox="0 0 12 16" fill="none" stroke="var(--white)" stroke-width="1.5"><path d="M6 15 C2 10 1 8 1 6 A5 5 0 0 1 11 6 C11 8 10 10 6 15 Z"/><circle cx="6" cy="6" r="2"/></svg>
      <span>MARYLAND OFFICE: 2150 Harbor Ridge Rd, Columbia, MD 21044</span>
      <span class="footer-sep"></span>
      <span>NMLS #318660</span>
    </div>
  </div>
</div>
</body>
</html>
```